International Consultancy Needs Slick Professional Presentation Graphic

Quarvel are an international engineering and advisory consultancy servicing the mining industry with a mix of Technology (Software), Services (consulting) and Systems (work structures).

We need a slick presentation graphic for use in presentation slides, whitepapers. I have attached a basic pic of the information we want to convey. Flat or 3D no preference, colouring no preference. Don't have to be circles, that was just easiest to draft up initially.

Industry/Entity Type

Mining

```html
<!DOCTYPE html>
<html lang="en">
<head>
<meta charset="utf-8">
<title>Quarvel Capability Model</title>
<link rel="stylesheet" href="https://fonts.googleapis.com/css2?family=Lato:wght@700;900&display=swap">
<style>
  :root {
    --bg: #ffffff;
    --blue-light: #2a8fd6;
    --blue-mid: #1b63b3;
    --blue-deep: #23328a;
    --lens-light: #13b4e8;
    --lens-mid: #0a88d0;
    --green-light: #a3d45a;
    --green-mid: #6cbd3c;
    --green-deep: #0c9644;
    --line: #ffffff;
    --text: #ffffff;
  }
  html, body {
    margin: 0;
    padding: 0;
    width: 1200px;
    height: 844px;
    overflow: hidden;
    background: var(--bg);
  }
  .capability-model {
    display: block;
    width: 1200px;
    height: 844px;
  }
  .label {
    font-family: "Lato", sans-serif;
    font-weight: 700;
    fill: var(--text);
    text-anchor: middle;
  }
  .label--domain { font-size: 20px; font-weight: 900; }
  .label--overlap { font-size: 15.5px; }
  .label--core { font-size: 24px; font-weight: 900; }
  .divider { fill: none; stroke: var(--line); stroke-width: 5; }
  .icon { fill: var(--text); }
  .icon-line { stroke: var(--text); stroke-width: 2.5; fill: none; }
</style>
</head>
<body>
<svg class="capability-model" viewBox="0 0 1200 844" xmlns="http://www.w3.org/2000/svg" role="img" aria-label="Capability model: Technology, People and Systems overlapping">
  <defs>
    <linearGradient id="grad-technology" x1="0" y1="0" x2="1" y2="1">
      <stop offset="0" stop-color="var(--blue-light)"/>
      <stop offset="1" stop-color="var(--blue-mid)"/>
    </linearGradient>
    <linearGradient id="grad-people" x1="0" y1="0" x2="1" y2="1">
      <stop offset="0" stop-color="var(--blue-mid)"/>
      <stop offset="1" stop-color="var(--blue-deep)"/>
    </linearGradient>
    <linearGradient id="grad-systems" x1="0" y1="0" x2="1" y2="1">
      <stop offset="0" stop-color="var(--blue-mid)"/>
      <stop offset="0.7" stop-color="var(--blue-mid)"/>
      <stop offset="1" stop-color="var(--blue-light)"/>
    </linearGradient>
    <linearGradient id="grad-lens" x1="0" y1="0" x2="0" y2="1">
      <stop offset="0" stop-color="var(--lens-light)"/>
      <stop offset="1" stop-color="var(--lens-mid)"/>
    </linearGradient>
    <linearGradient id="grad-core" x1="0" y1="0" x2="0" y2="1">
      <stop offset="0" stop-color="var(--green-light)"/>
      <stop offset="0.5" stop-color="var(--green-mid)"/>
      <stop offset="1" stop-color="var(--green-deep)"/>
    </linearGradient>
    <clipPath id="clip-technology"><circle cx="513" cy="340" r="168"/></clipPath>
    <clipPath id="clip-people"><circle cx="681" cy="340" r="168"/></clipPath>
    <clipPath id="clip-systems"><circle cx="597" cy="487" r="168"/></clipPath>
  </defs>

  <!-- domains -->
  <circle cx="513" cy="340" r="168" fill="url(#grad-technology)"/>
  <circle cx="681" cy="340" r="168" fill="url(#grad-people)"/>
  <circle cx="597" cy="487" r="168" fill="url(#grad-systems)"/>

  <!-- overlaps -->
  <g clip-path="url(#clip-technology)">
    <circle cx="681" cy="340" r="168" fill="url(#grad-lens)"/>
    <circle cx="597" cy="487" r="168" fill="url(#grad-lens)"/>
  </g>
  <g clip-path="url(#clip-people)">
    <circle cx="597" cy="487" r="168" fill="url(#grad-lens)"/>
  </g>
  <g clip-path="url(#clip-technology)">
    <g clip-path="url(#clip-people)">
      <circle cx="597" cy="487" r="168" fill="url(#grad-core)"/>
    </g>
  </g>

  <!-- dividing lines -->
  <g clip-path="url(#clip-people)"><circle class="divider" cx="513" cy="340" r="168"/></g>
  <g clip-path="url(#clip-systems)"><circle class="divider" cx="513" cy="340" r="168"/></g>
  <g clip-path="url(#clip-technology)"><circle class="divider" cx="681" cy="340" r="168"/></g>
  <g clip-path="url(#clip-systems)"><circle class="divider" cx="681" cy="340" r="168"/></g>
  <g clip-path="url(#clip-technology)"><circle class="divider" cx="597" cy="487" r="168"/></g>
  <g clip-path="url(#clip-people)"><circle class="divider" cx="597" cy="487" r="168"/></g>

  <!-- icons -->
  <g class="icon icon-gears">
    <g transform="translate(429 267)">
      <circle r="12"/>
      <g>
        <rect x="-4" y="-18" width="8" height="36"/>
        <rect x="-4" y="-18" width="8" height="36" transform="rotate(45)"/>
        <rect x="-4" y="-18" width="8" height="36" transform="rotate(90)"/>
        <rect x="-4" y="-18" width="8" height="36" transform="rotate(135)"/>
      </g>
      <circle r="6" fill="var(--blue-light)"/>
    </g>
    <g transform="translate(458 253)">
      <circle r="8"/>
      <rect x="-3" y="-12" width="6" height="24"/>
      <rect x="-3" y="-12" width="6" height="24" transform="rotate(45)"/>
      <rect x="-3" y="-12" width="6" height="24" transform="rotate(90)"/>
      <rect x="-3" y="-12" width="6" height="24" transform="rotate(135)"/>
      <circle r="4" fill="var(--blue-light)"/>
    </g>
  </g>
  <g class="icon icon-people">
    <ellipse cx="768" cy="258" rx="8" ry="10"/>
    <path d="M755 282 q0 -14 13 -14 q13 0 13 14 z"/>
    <ellipse cx="749" cy="260" rx="10" ry="12" stroke="var(--blue-mid)" stroke-width="2"/>
    <path d="M731 285 q0 -17 18 -17 q18 0 18 17 z" stroke="var(--blue-mid)" stroke-width="2"/>
  </g>
  <g class="icon icon-network">
    <path class="icon-line" d="M585 528 v20 M605 522 v26 M578 548 h45 M594 548 v10 M610 548 h10"/>
    <rect x="580" y="522" width="9" height="9"/>
    <rect x="600" y="516" width="9" height="9"/>
    <rect x="590" y="554" width="9" height="9"/>
    <rect x="616" y="543" width="9" height="9"/>
  </g>

  <!-- labels -->
  <text class="label label--domain" x="435" y="323">Technology</text>
  <text class="label label--domain" x="760" y="323">People</text>
  <text class="label label--domain" x="595" y="587">Systems</text>

  <text class="label label--overlap" x="597" y="254">User</text>
  <text class="label label--overlap" x="597" y="274">Interface</text>
  <text class="label label--overlap" x="597" y="294">Engineering</text>

  <text class="label label--overlap" x="494" y="430">System</text>
  <text class="label label--overlap" x="494" y="450">Interface</text>
  <text class="label label--overlap" x="494" y="470">Engineering</text>

  <text class="label label--overlap" x="704" y="445">Organisation</text>
  <text class="label label--overlap" x="704" y="465">Design</text>

  <text class="label label--core" x="598" y="389">Capability</text>
</svg>
</body>
</html>
```